Company Website

We need an interactive website designed that for new company. Our company is in the Automotive fleet maintenance business. We have wide ranging customers in many industries e.g Aviation industry, construction industry, transportation etc.
We would like the website to have login accounts where customers can register, login and access their service history. Also we would like to have an appointment system where customers could schedule appointments, once appointments are made that time would no longer be available to be selected as it would be booked etc.

The website should also be updatable and provide areas for showcasing
Our services
Products/parts (possibly store front)
Customer feedback
Appointments
Our customers (where our customers can advertise or be showcased)
About us
Contacts
gallery

We would like designs that have a modern, corporate feel, One that is user friendly.
prefer a design that does not look like a template.

Target Market(s)

Medium to large companies, small business owners and the general motoring public.

Industry/Entity Type

Construction

Requirements
Must have
• Customer login set up so a database of customer vehicle maintenance history as well as the ability to schedule repairs via their account. They could also check the status of a repair.
Nice to have
• Photo gallery to show case current projects.
Our customers page where we can show case our clients they could also post their events on there, promotions etc.

The theme Should be something that's reflective of our core business; fleet maintenance. It would be nice to capture some sort of background in there that depicts some of that for example mixer trucks, tractors,loaders excavators forklifts cars trucks. That's what we deal with. It's up to the designer to capture the Essence of this as much as possible. Impress me.
Should not have
• Would prefer a custom website not a template.

```html
<!DOCTYPE html>
<html lang="en">
<head>
<meta charset="utf-8">
<title>Keystone Fleet &amp; Auto Maintenance</title>
<link href="https://fonts.googleapis.com/css2?family=Oswald:wght@400;500&family=Open+Sans:wght@400;600;700&display=swap" rel="stylesheet">
<style>
:root{
  --red:#c1121c;
  --red-dark:#a50f17;
  --black:#0c0c0c;
  --ink:#333;
  --muted:#555;
  --line:#cfcfcf;
  --panel:#cfcfcf;
  --white:#fff;
}
*{box-sizing:border-box;margin:0;padding:0}
html,body{width:958px;height:1200px;overflow:hidden;background:var(--white);font-family:"Open Sans",sans-serif;color:var(--ink)}
.page{position:relative;width:958px;height:1200px}
.abs{position:absolute}

/* header */
.site-header{position:absolute;left:0;top:0;width:958px;height:74px;background:var(--black)}
.brand{position:absolute;left:140px;top:24px;display:flex;align-items:center;gap:8px}
.brand-mark{width:14px;height:14px;background:var(--red)}
.brand-name{font-family:"Oswald",sans-serif;font-weight:500;font-size:20px;color:var(--white);letter-spacing:.5px;line-height:1;white-space:nowrap}
.account{position:absolute;right:140px;top:7px;display:flex;gap:14px;font-size:9px;color:var(--white)}
.account span{display:flex;align-items:center;gap:5px}
.main-nav{position:absolute;left:340px;top:49px;display:flex;gap:13px;font-size:10px;color:var(--white);align-items:center;white-space:nowrap}

/* hero */
.hero{position:absolute;left:0;top:74px;width:958px;height:287px;background:linear-gradient(180deg,#b9c9da 0%,#dfe7ee 45%,#9b9fa3 80%,#7c7f82 100%)}
.dots{position:absolute;left:436px;top:333px;display:flex;gap:8px}
.dots i{width:15px;height:15px;border-radius:50%;background:#e6e6e6;display:block}
.dots i.on{background:var(--red);border:2px solid #fff}

/* section headings */
.heading{font-family:"Oswald",sans-serif;font-weight:400;color:var(--red);text-transform:uppercase;font-size:16px;line-height:1;white-space:nowrap}
.rule{height:2px;background:var(--line)}

/* project cards */
.card{position:absolute;top:425px;width:208px;height:188px;border:1px solid #ddd;border-bottom:4px solid var(--red);background:var(--white)}
.card-photo{height:109px}
.card h3{font-family:"Oswald",sans-serif;font-weight:400;font-size:15px;color:#222;margin:7px 12px 4px;white-space:nowrap}
.card p{font-size:8.6px;line-height:13px;color:var(--muted);margin:0 12px}

/* welcome */
.intro{font-size:8.8px;line-height:13.4px;color:var(--muted);width:272px}
.read-more{font-size:7.5px;color:var(--red)}
.features{display:grid;grid-template-columns:178px 178px;row-gap:11px;font-size:11px;color:#444}
.features li{list-style:none;display:flex;align-items:center;gap:12px;height:16px;white-space:nowrap}
.tick{width:15px;height:15px;border:1px solid #ccc;background:#f2f2f2;display:flex;align-items:center;justify-content:center}

/* customers */
.client{font-size:14px;font-weight:600;width:90px;text-align:center}
.slide-btn{width:22px;height:22px;background:#ddd;display:flex;align-items:center;justify-content:center}

/* news */
.news-item{position:absolute;left:603px;width:205px;display:flex;gap:9px}
.date{flex:none;width:30px;height:33px;background:#555;color:#fff;font-family:"Oswald",sans-serif;font-size:11px;line-height:12px;text-align:center;padding-top:4px}
.news-item b{font-size:8.4px;color:#111;display:block;white-space:nowrap}
.news-item p{font-size:7.6px;line-height:9px;color:#555}

/* appointment */
.appointment{position:absolute;left:604px;top:785px;width:200px;height:227px;background:var(--panel);border-radius:4px;padding:8px 12px}
.appointment h2{font-family:"Open Sans",sans-serif;font-weight:400;font-size:15px;color:#444;margin-bottom:7px;white-space:nowrap}
.field{height:18px;background:#fff;border:1px solid #bbb;border-radius:3px;font-size:8.6px;color:#444;padding:2px 8px;margin-bottom:7px}
.row{display:flex;gap:8px}
.row .field{display:flex;align-items:center;justify-content:space-between;white-space:nowrap;padding:0 5px 0 8px}
.btn{background:var(--red);color:#fff;font-weight:700;font-size:9px;display:inline-flex;align-items:center;justify-content:center;border-radius:2px}

/* footer */
.site-footer{position:absolute;left:0;top:1048px;width:958px;height:152px;background:var(--black);border-top:3px solid var(--red);color:#fff}
.site-footer h4{font-size:12.5px;font-weight:600;white-space:nowrap}
.col-sep{position:absolute;top:16px;width:1px;height:130px;background:#333}
.quick li{list-style:none;font-size:8px;line-height:13.3px;display:flex;gap:8px;align-items:center}
.quick li::before{content:"";border-left:4px solid #888;border-top:3px solid transparent;border-bottom:3px solid transparent}
.small{font-size:8px;line-height:13.5px}
.social{display:flex;gap:6px}
.social i{width:17px;height:17px;background:#1f5fa8;display:block}
</style>
</head>
<body>
<div class="page">

<header class="site-header">
  <div class="brand"><span class="brand-mark"></span><span class="brand-name">KEYSTONE FLEET &amp; AUTO</span></div>
  <div class="account">
    <span><svg width="9" height="9" viewBox="0 0 10 10"><circle cx="5" cy="3" r="2.4" fill="#c1121c"/><path d="M1 10c0-3 2-4.5 4-4.5S9 7 9 10z" fill="#c1121c"/></svg>Login</span>
    <span style="border-left:1px solid #444;padding-left:8px"><svg width="9" height="9" viewBox="0 0 10 10"><rect x="1" y="2" width="7" height="7" fill="none" stroke="#c1121c"/><path d="M4 6l5-5" stroke="#c1121c"/></svg>Register</span>
  </div>
  <nav class="main-nav">
    <svg width="15" height="13" viewBox="0 0 15 13"><path d="M7.5 0L0 6.5h2V13h4V9h3v4h4V6.5h2z" fill="#c1121c"/></svg>
    <span>About Us</span><span>Our Services</span><span>Products/Parts</span><span>Customer Feedback</span><span>Our Customers</span><span>Gallery</span><span>Contacts</span>
  </nav>
</header>

<section class="hero" role="img" aria-label="Technician in hard hat holding a clipboard in front of a row of white fleet trucks under a cloudy sky"></section>
<div class="dots"><i class="on"></i><i></i><i></i><i></i></div>

<!-- current projects -->
<div class="abs rule" style="left:144px;top:404px;width:248px"></div>
<div class="abs rule" style="left:568px;top:404px;width:242px"></div>
<h2 class="abs heading" style="left:400px;top:393px;width:160px;text-align:center;font-size:19px">Current Projects</h2>

<svg class="abs" style="left:118px;top:500px" width="14" height="24" viewBox="0 0 14 24"><path d="M12 2L3 12l9 10" fill="none" stroke="#666" stroke-width="2.5"/></svg>
<svg class="abs" style="left:824px;top:500px" width="14" height="24" viewBox="0 0 14 24"><path d="M2 2l9 10-9 10" fill="none" stroke="#666" stroke-width="2.5"/></svg>

<article class="card" style="left:144px">
  <div class="card-photo" role="img" aria-label="Long row of white semi trucks parked in a line" style="background:linear-gradient(180deg,#b7c6d6,#d8dde2 55%,#8d8f8f)"></div>
  <h3>Duis autem vel eum iriure dolor</h3>
  <p>Lorem ipsum dolor sit amet, consectetuer adipiscing elit, sed diam nonummy nibh euismod tincidunt ut laoreet dolore</p>
</article>
<article class="card" style="left:373px">
  <div class="card-photo" role="img" aria-label="Mechanic in blue overalls servicing a heavy wheel hub in a workshop" style="background:linear-gradient(135deg,#8e9a6a,#5d6a7c 60%,#2f3a52)"></div>
  <h3>Duis autem vel eum iriure dolor</h3>
  <p>Lorem ipsum dolor sit amet, consectetuer adipiscing elit, sed diam nonummy nibh euismod tincidunt ut laoreet dolore</p>
</article>
<article class="card" style="left:603px">
  <div class="card-photo" role="img" aria-label="Ground crew refuelling a grey military helicopter" style="background:linear-gradient(135deg,#4f6aa8,#7c838b 55%,#5e6468)"></div>
  <h3>Duis autem vel eum iriure dolor</h3>
  <p>Lorem ipsum dolor sit amet, consectetuer adipiscing elit, sed diam nonummy nibh euismod tincidunt ut laoreet dolore</p>
</article>

<!-- welcome -->
<h2 class="abs heading" style="left:140px;top:638px">Welcome to Keystone Fleet &amp; Auto Maintenance</h2>
<div class="abs" style="left:141px;top:665px;width:152px;height:101px;background:#222">
  <div role="img" aria-label="Video still of technicians standing beside service vehicles" style="height:79px;background:linear-gradient(180deg,#c9d3dc,#8c949a 60%,#5b6066)"></div>
  <div style="height:3px;background:var(--red)"></div>
  <svg class="abs" style="left:65px;top:28px" width="24" height="24" viewBox="0 0 24 24"><circle cx="12" cy="12" r="11" fill="rgba(0,0,0,.55)" stroke="#fff"/><path d="M9 7l8 5-8 5z" fill="#fff"/></svg>
  <div class="abs" style="left:36px;top:88px;font-size:6.5px;color:#fff">0:00</div>
  <svg class="abs" style="left:14px;top:88px" width="16" height="8" viewBox="0 0 16 8"><path d="M0 0l6 4-6 4z" fill="#ccc"/><path d="M10 3h2l3-3v8l-3-3h-2z" fill="#ccc"/></svg>
</div>
<p class="abs intro" style="left:310px;top:665px">Lorem ipsum dolor sit amet, consectetuer adipiscing elit, sed diam nonummy nibh euismod tincidunt ut laoreet dolore magna amet aliquam erat volutpat. Ut wisi enim ad minim veniam, quis exerci tation ullamcorper suscipit lobortis nisl ut aliquip ex ea commodo consequat. Duis autem vel eum iriure dolor in hendrerit in amet sit vulputate velit esse molestie consequat, vel illum dolore eu amet feugiat nulla facilisis at vero eros et accumsan.</p>
<span class="abs read-more" style="left:539px;top:758px">Read More</span>

<h2 class="abs heading" style="left:140px;top:790px;text-transform:none">Factory certified technicians and over 40years combined experience</h2>
<ul class="abs features" style="left:141px;top:818px">
  <li><span class="tick"><svg width="6" height="6" viewBox="0 0 6 6"><path d="M1 0l4 3-4 3z" fill="#555"/></svg></span>Complete Refurbishing</li>
  <li><span class="tick"><svg width="6" height="6" viewBox="0 0 6 6"><path d="M1 0l4 3-4 3z" fill="#555"/></svg></span>Mobile Service Vehicles</li>
  <li><span class="tick"><svg width="6" height="6" viewBox="0 0 6 6"><path d="M1 0l4 3-4 3z" fill="#555"/></svg></span>Zero-time Rebuilds</li>
  <li><span class="tick"><svg width="6" height="6" viewBox="0 0 6 6"><path d="M1 0l4 3-4 3z" fill="#555"/></svg></span>Refueling Services</li>
  <li><span class="tick"><svg width="6" height="6" viewBox="0 0 6 6"><path d="M1 0l4 3-4 3z" fill="#555"/></svg></span>Engine repair/rebuilds</li>
  <li><span class="tick"><svg width="6" height="6" viewBox="0 0 6 6"><path d="M1 0l4 3-4 3z" fill="#555"/></svg></span>Highly Skilled Technicians</li>
  <li><span class="tick"><svg width="6" height="6" viewBox="0 0 6 6"><path d="M1 0l4 3-4 3z" fill="#555"/></svg></span>Transmission</li>
  <li><span class="tick"><svg width="6" height="6" viewBox="0 0 6 6"><path d="M1 0l4 3-4 3z" fill="#555"/></svg></span>Fleet repair</li>
</ul>

<!-- customers -->
<h2 class="abs heading" style="left:140px;top:946px">Our Customers</h2>
<div class="abs rule" style="left:246px;top:957px;width:340px"></div>
<div class="abs slide-btn" style="left:143px;top:985px"><svg width="6" height="9" viewBox="0 0 6 9"><path d="M5 1L1 4.5 5 8" fill="none" stroke="#fff" stroke-width="1.5"/></svg></div>
<div class="abs slide-btn" style="left:562px;top:985px"><svg width="6" height="9" viewBox="0 0 6 9"><path d="M1 1l4 3.5L1 8" fill="none" stroke="#fff" stroke-width="1.5"/></svg></div>
<div class="abs" style="left:175px;top:986px;display:flex;gap:6px;align-items:center;height:20px">
  <span class="client" style="color:#2a3566">Corvell</span>
  <span class="client" style="color:#243a7a">Brightwell</span>
  <span class="client" style="color:#1f4d9b">Halvion</span>
  <span class="client" style="color:#1e6ea6">Ostrava</span>
</div>

<!-- news -->
<h2 class="abs heading" style="left:604px;top:638px;font-size:18px">Latest News</h2>
<div class="abs rule" style="left:708px;top:650px;width:100px"></div>
<div class="news-item" style="top:666px">
  <div class="date">08<br>OCT</div>
  <div><b>Lorem Ipsum dolor sit amet, consectet</b><p>Lorem ipsum dolor sit amet, consectetuer adipiscing elit.</p></div>
</div>
<div class="abs" style="left:643px;top:707px;width:165px;height:1px;background:#e2e2e2"></div>
<div class="news-item" style="top:713px">
  <div class="date">15<br>OCT</div>
  <div><b>Lorem Ipsum dolor sit amet, consectet</b><p>Lorem ipsum dolor sit amet, consectetuer adipiscing elit.</p></div>
</div>
<div class="abs" style="left:603px;top:762px;width:146px;height:2px;background:var(--red)"></div>
<span class="abs read-more" style="left:755px;top:758px">View All News</span>

<form class="appointment">
  <h2>Make An Appointment</h2>
  <div class="field">Name</div>
  <div class="field">Email</div>
  <div class="field">Phone</div>
  <div class="field">Company Name</div>
  <div class="row">
    <div class="field" style="width:80px">Date<svg width="11" height="11" viewBox="0 0 11 11"><rect x=".5" y=".5" width="10" height="10" fill="#fff" stroke="#888"/><path d="M3 4l2.5 3L8 4z" fill="#444"/></svg></div>
    <div class="field" style="width:46px">8 : 00<svg width="6" height="11" viewBox="0 0 6 11"><path d="M3 0l3 4H0zM3 11l3-4H0z" fill="#555"/></svg></div>
    <div class="field" style="width:34px;padding:0 4px 0 5px">AM<svg width="6" height="11" viewBox="0 0 6 11"><path d="M3 0l3 4H0zM3 11l3-4H0z" fill="#555"/></svg></div>
  </div>
  <div class="field" style="height:36px">Comments</div>
  <div class="btn" style="width:62px;height:18px">SUBMIT</div>
</form>

<!-- footer -->
<footer class="site-footer">
  <h4 class="abs" style="left:143px;top:16px">Quick Links</h4>
  <ul class="abs quick" style="left:148px;top:36px">
    <li>Home</li><li>About Us</li><li>Our Services</li><li>Products/Parts</li><li>Customer Feedback</li><li>Our Customers</li><li>Gallery</li><li>Contacts</li>
  </ul>
  <div class="col-sep" style="left:261px"></div>
  <h4 class="abs" style="left:288px;top:16px">Get A Newsletter</h4>
  <p class="abs small" style="left:292px;top:36px;width:140px">Get the latest updates by entering your email address</p>
  <div class="abs" style="left:289px;top:73px;width:131px;height:18px;background:#555;font-size:8px;font-style:italic;color:#ddd;padding:3px 6px">email address</div>
  <div class="abs btn" style="left:289px;top:105px;width:82px;height:20px">SUBSCRIBE</div>
  <div class="col-sep" style="left:448px"></div>
  <h4 class="abs" style="left:475px;top:16px">Contact Details</h4>
  <svg class="abs" style="left:477px;top:41px" width="9" height="12" viewBox="0 0 9 12"><path d="M4.5 0A4.5 4.5 0 0 0 0 4.5C0 8 4.5 12 4.5 12S9 8 9 4.5A4.5 4.5 0 0 0 4.5 0z" fill="#fff"/><circle cx="4.5" cy="4.5" r="1.6" fill="#000"/></svg>
  <p class="abs small" style="left:494px;top:37px;width:112px">Lorem ipsum dolor sit amet, consectetur adipiscing elit. site amet</p>
  <svg class="abs" style="left:477px;top:89px" width="10" height="10" viewBox="0 0 10 10"><path d="M2 0l2 2.5-1 1.5c.8 1.5 1.6 2.3 3 3l1.5-1L10 8 8.5 10C4 9.5.5 6 0 1.5z" fill="#fff"/></svg>
  <p class="abs small" style="left:494px;top:87px">123-456-7890</p>
  <svg class="abs" style="left:476px;top:107px" width="12" height="9" viewBox="0 0 12 9"><rect width="12" height="9" fill="#fff"/><path d="M0 0l6 5 6-5" fill="none" stroke="#000"/></svg>
  <p class="abs small" style="left:494px;top:104px">info@keystonefleet.com</p>
  <div class="col-sep" style="left:625px"></div>
  <div class="abs" style="left:656px;top:24px;display:flex;align-items:center;gap:7px"><span class="brand-mark"></span><span class="brand-name" style="font-size:17px">KEYSTONE FLEET &amp; AUTO</span></div>
  <p class="abs small" style="left:660px;top:81px;width:150px;text-align:center;line-height:12px">Copyright 2014 Keystone Fleet &amp; Auto Maintenance</p>
  <div class="abs social" style="left:701px;top:115px"><i></i><i style="background:#2a9bd8"></i><i style="background:#1a6fa8"></i></div>
</footer>

</div>
</body>
</html>
```